Top International Talent Management Needs creative business card design

We manage actors careers and book them liaising and promoting their profiles internationally through Casting Directors, Producers, Directors, Publicists etc. We need clearly visable contact details but with a design that reflects our status and creativity of TV, Feature Film industry. Our logo is attached and needs to relate and our website is www.marrowlanepeople.com
No flame designs please but please incorporate logo colours.

Target Market(s)

Clients

Industry/Entity Type

Film Production

Contact Information for Business Card

Director Rosalind Tebbett
Suite F, Building 4, Harrowgate Sound Stages, Tullick Vale, Sydney, NSW 2021

Font styles to use
Sans Serif

Colors
ec1f27

Requirements
Nice to have
• Colours should relate to logo attached and type can relate again to type in the logo design.
Should not have
• No Flames designs and best to be not too obvious with the film designs eiither. Needs to be more creative and modern

```html
<!DOCTYPE html>
<html lang="en">
<head>
<meta charset="utf-8">
<title>Marrow Lane People — Business Card Back</title>
<link rel="stylesheet" href="https://fonts.googleapis.com/css2?family=Source+Sans+3:wght@400;600&display=swap">
<style>
  :root {
    --ink: #262626;
    --signal-red: #ec1f27;
    --paper: #ffffff;
    --text-light: #ffffff;
  }
  html, body {
    margin: 0;
    padding: 0;
    overflow: hidden;
    background: var(--paper);
  }
  .card {
    position: relative;
    width: 1200px;
    height: 720px;
    background: var(--paper);
    overflow: hidden;
    font-family: "Source Sans 3", sans-serif;
  }
  .card__bands {
    position: absolute;
    inset: 0;
    width: 1200px;
    height: 720px;
  }
  .band--dark { fill: var(--ink); }
  .band--red { fill: var(--signal-red); }

  .brand-name {
    position: absolute;
    left: 146px;
    top: 300px;
    margin: 0;
    font-size: 46px;
    font-weight: 600;
    line-height: 1;
    letter-spacing: 0.5px;
    color: var(--signal-red);
  }

  .social-panel {
    position: absolute;
    left: 628px;
    top: 270px;
    width: 572px;
    height: 179px;
    background: var(--ink);
    box-sizing: border-box;
    padding: 48px 0 0 40px;
  }
  .social-list {
    list-style: none;
    margin: 0;
    padding: 0;
  }
  .social-list__item {
    display: flex;
    align-items: center;
    height: 50px;
    color: var(--text-light);
    font-size: 29px;
    font-weight: 400;
  }
  .social-list__marker {
    width: 18px;
    height: 18px;
    margin: 0 30px 0 7px;
    background: var(--signal-red);
    flex: none;
  }
</style>
</head>
<body>
  <main class="card">
    <svg class="card__bands" viewBox="0 0 1200 720" aria-hidden="true">
      <polygon class="band--dark" points="0,0 176,0 0,581"/>
      <polygon class="band--red" points="1056,0 1200,0 1200,720 837,720"/>
    </svg>

    <h1 class="brand-name">Marrow Lane People</h1>

    <section class="social-panel" aria-label="Social profiles">
      <ul class="social-list">
        <li class="social-list__item"><span class="social-list__marker"></span>friendwall.com/MarrowLanePeople</li>
        <li class="social-list__item"><span class="social-list__marker"></span>chirpline.com/marrowlanepeople</li>
      </ul>
    </section>
  </main>
</body>
</html>
```